Creating a Label for the Wine "Brenola"

Brenola
As you know Brenola is an imagined place or state of things in which everything is perfect. This wine reflects that. It is a high value wine and it is perfect. The dimensions shoulb be between 9c x 11,5 cm and 12cm x 8 cm

```html
<!DOCTYPE html>
<html lang="en">
<head>
<meta charset="utf-8">
<title>Brenola – Prestige Wine Label</title>
<link href="https://fonts.googleapis.com/css2?family=Raleway:wght@300;400;500&display=swap" rel="stylesheet">
<style>
  :root {
    --backdrop: #121212;
    --label-black: #050505;
    --gold: #c9b92a;
    --gold-soft: #9e9224;
    --ivory: #ece6c2;
  }
  html, body {
    margin: 0;
    padding: 0;
    width: 1200px;
    height: 1000px;
    overflow: hidden;
    background: var(--backdrop);
  }
  .canvas {
    position: relative;
    width: 1200px;
    height: 1000px;
    background: var(--backdrop);
    font-family: "Raleway", sans-serif;
  }
  .wine-label {
    position: absolute;
    left: 290px;
    top: 100px;
    width: 620px;
    height: 800px;
    background: var(--label-black);
    color: var(--ivory);
  }
  .label-frame {
    position: absolute;
    inset: 0;
  }
  .accent-dot {
    position: absolute;
    left: 50%;
    width: 16px;
    height: 16px;
    margin-left: -8px;
    border-radius: 50%;
    background: var(--gold-soft);
  }
  .accent-dot--top { top: 88px; }
  .accent-dot--bottom { top: 612px; }
  .brand-mark {
    position: absolute;
    left: 0;
    right: 0;
    top: 330px;
    text-align: center;
  }
  .brand-name {
    margin: 0;
    font-weight: 300;
    font-size: 68px;
    letter-spacing: 4px;
    color: var(--ivory);
    text-transform: uppercase;
  }
  .brand-rule {
    width: 330px;
    height: 2px;
    margin: 18px auto 0;
    background: var(--gold);
  }
  .wine-type {
    position: absolute;
    left: 0;
    right: 0;
    top: 478px;
    margin: 0;
    text-align: center;
    font-weight: 400;
    font-size: 20px;
    letter-spacing: 3px;
    color: var(--ivory);
  }
  .wine-notes {
    position: absolute;
    left: 0;
    right: 0;
    top: 516px;
    margin: 0;
    text-align: center;
    font-weight: 300;
    font-size: 13px;
    line-height: 22px;
    letter-spacing: 1.5px;
    color: var(--gold-soft);
  }
  .wine-spec {
    position: absolute;
    top: 666px;
    margin: 0;
    font-weight: 400;
    font-size: 15px;
    letter-spacing: 1px;
    color: var(--ivory);
  }
  .wine-spec--strength { left: 72px; }
  .wine-spec--volume { right: 72px; }
</style>
</head>
<body>
<main class="canvas">
  <section class="wine-label" aria-label="Brenola wine label">
    <svg class="label-frame" width="620" height="800" viewBox="0 0 620 800" aria-hidden="true">
      <rect x="14" y="14" width="592" height="772" fill="none" stroke="var(--gold)" stroke-width="3"/>
      <path d="M44 36 H576 V44 H584 V756 H576 V764 H44 V756 H36 V44 H44 Z"
            fill="none" stroke="var(--gold-soft)" stroke-width="2"/>
    </svg>

    <span class="accent-dot accent-dot--top"></span>

    <div class="brand-mark">
      <h1 class="brand-name">Brenola</h1>
      <div class="brand-rule"></div>
    </div>

    <p class="wine-type">PRESTIGE WINE</p>
    <p class="wine-notes">Estate bottled red wine<br>Aged in oak barrels</p>

    <span class="accent-dot accent-dot--bottom"></span>

    <p class="wine-spec wine-spec--strength">12% vol.</p>
    <p class="wine-spec wine-spec--volume">750 ml</p>
  </section>
</main>
</body>
</html>
```